Church Bulletin Ad (see attached sample)

Create a New Church Bulletin Ad. I have attached some samples of what we would like to have in the ad. (1) Marrowfield Realty Thorne Logo (2) Headshot (3) Lena Vasko & Greta Vasko, Real Estate Team (4) Phone number (5) Email address (6) St Aldwin Parishioners for over 40 Years. We would like for the ad to be clean and modern. NO OTHER IMAGES besides headshots and Marrowfield Realty Thorne Logo.

Target Market(s)

Church community

Industry/Entity Type

Real Estate

Font styles to use
Sans Serif
Other font styles liked:
• Modern Font

Colors
0054AA
0677BA
7BADD7
CADEEF
E8F1F8

Requirements
Must have
• Marrowfield Realty Thorne Logo; Headshot; Ad size is 4.5"x1.62"

```html
<!DOCTYPE html>
<html lang="en">
<head>
<meta charset="UTF-8">
<title>St Aldwin Bulletin Ad – Lena Vasko &amp; Greta Vasko</title>
<link rel="stylesheet" href="https://fonts.googleapis.com/css2?family=Open+Sans:ital,wght@0,400;0,600;0,700;1,400&display=swap">
<style>
  :root {
    --blue-deep: #0054aa;
    --blue-mid: #0677ba;
    --blue-soft: #7badd7;
    --blue-pale: #cadeef;
    --blue-mist: #e8f1f8;
    --navy: #1b2f5e;
    --ink: #12305f;
    --white: #ffffff;
  }
  * { box-sizing: border-box; margin: 0; padding: 0; }
  html, body {
    width: 1200px;
    height: 432px;
    overflow: hidden;
    background: var(--white);
  }
  .ad {
    position: relative;
    width: 1200px;
    height: 432px;
    overflow: hidden;
    font-family: "Open Sans", Arial, sans-serif;
    background: linear-gradient(135deg, var(--blue-mist) 0%, #f4f8fc 45%, var(--blue-pale) 100%);
  }
  .ad__waves {
    position: absolute;
    inset: 0;
    width: 100%;
    height: 100%;
  }
  .banner {
    position: absolute;
    left: 80px;
    top: 18px;
    width: 1085px;
    height: 62px;
    background: linear-gradient(90deg, var(--blue-mid) 0%, var(--blue-deep) 100%);
    box-shadow: 4px 5px 8px rgba(18, 48, 95, 0.35);
    display: flex;
    align-items: center;
    justify-content: center;
  }
  .banner__text {
    color: var(--white);
    font-weight: 700;
    font-size: 34px;
    letter-spacing: 0.2px;
  }
  .banner__text strong { font-weight: 700; color: var(--white); }
  .headshot {
    position: absolute;
    left: 44px;
    top: 121px;
    width: 432px;
    height: 267px;
    background: linear-gradient(180deg, #dfe6ec 0%, #c9ccd0 55%, #3a3536 100%);
  }
  .tagline {
    position: absolute;
    left: 512px;
    top: 118px;
    font-size: 31px;
    font-weight: 700;
    color: var(--blue-deep);
    letter-spacing: 0.5px;
    white-space: nowrap;
  }
  .team {
    position: absolute;
    left: 512px;
    top: 196px;
    color: var(--ink);
  }
  .team__names {
    font-size: 32px;
    font-weight: 700;
    color: var(--blue-deep);
    white-space: nowrap;
    line-height: 1.15;
  }
  .team__role {
    font-size: 26px;
    font-style: italic;
    color: var(--blue-deep);
    line-height: 1.3;
  }
  .team__phone {
    margin-top: 6px;
    font-size: 38px;
    font-weight: 700;
    color: var(--blue-deep);
    letter-spacing: 0.5px;
  }
  .brand {
    position: absolute;
    left: 1008px;
    top: 204px;
    width: 126px;
    height: 134px;
    background: var(--navy);
    display: flex;
    align-items: center;
    justify-content: center;
    text-align: center;
    padding: 8px;
  }
  .brand__name {
    color: var(--white);
    font-size: 17px;
    font-weight: 600;
    line-height: 1.25;
  }
  .contact-email {
    position: absolute;
    right: 41px;
    top: 366px;
    font-size: 24px;
    color: var(--ink);
    white-space: nowrap;
  }
</style>
</head>
<body>
<div class="ad">
  <svg class="ad__waves" viewBox="0 0 1200 432" preserveAspectRatio="none" aria-hidden="true">
    <path d="M0 300 C 300 240, 700 420, 1200 300 L1200 432 L0 432 Z" fill="#cadeef" opacity="0.35"/>
    <path d="M0 360 C 400 300, 800 440, 1200 360" fill="none" stroke="#ffffff" stroke-width="3" opacity="0.6"/>
  </svg>

  <header class="banner">
    <h1 class="banner__text">St Aldwin Parishioners for over <strong>40 Years!</strong></h1>
  </header>

  <div class="headshot" role="img" aria-label="Headshot of Lena Vasko and Greta Vasko"></div>

  <p class="tagline">ENERGY · EXCELLENCE · EXPERIENCE</p>

  <section class="team">
    <p class="team__names">Lena Vasko &amp; Greta Vasko</p>
    <p class="team__role">Real Estate Team</p>
    <p class="team__phone">(206) 555-0184</p>
  </section>

  <div class="brand">
    <span class="brand__name">Marrowfield Realty Thorne</span>
  </div>

  <p class="contact-email">email : vaskoteam@marrowfieldrt.com</p>
</div>
</body>
</html>
```